I am wanting to develop a new range of products called “SWIFT SERIES”. It will be 500mL trigger bottles of ready to use cleaning products. A Window&Glass Cleaner, Surface Sanitiser, Room Deodourant, Stainless Steel Rub, Spray&Wipe and a Sanitising Spray & Wipe. The label dimensions and shape are attached. Talbeck is the shape I want but I do not like the design so don't base your design on it. BLUEMAPLE is a design I like I also like the design on the coffee packaging.

Target Market(s)

Retail and commercial kitchen

Industry/Entity Type

Cleaning Product

```html
<!DOCTYPE html>
<html lang="en">
<head>
<meta charset="utf-8">
<title>Swift Series – Sanitising Spray &amp; Wipe Label</title>
<link rel="stylesheet" href="https://fonts.googleapis.com/css2?family=Oswald:wght@500;700&display=swap">
<style>
  :root {
    --page-bg: #f4f4f4;
    --label-top: #f7f7f7;
    --label-bottom: #e4e4e4;
    --ink-navy: #153b4f;
    --ink-dark: #2a2a2a;
    --eco-green: #6aad35;
    --eco-green-soft: #8cc152;
    --wave-light: #6fb1d6;
    --wave-mid: #2d87c0;
    --wave-deep: #0f4f74;
    --white: #ffffff;
  }
  * { margin: 0; padding: 0; box-sizing: border-box; }
  html, body {
    width: 964px;
    height: 1200px;
    overflow: hidden;
    background: var(--page-bg);
  }
  .label {
    position: absolute;
    left: 62px;
    top: 45px;
    width: 840px;
    height: 1110px;
    border-radius: 70px 70px 60px 60px;
    background: linear-gradient(180deg, var(--label-top) 0%, var(--label-bottom) 70%);
    overflow: hidden;
    font-family: "Oswald", sans-serif;
  }
  .brand-name {
    position: absolute;
    top: 148px;
    left: 0;
    width: 100%;
    text-align: center;
    font-weight: 700;
    font-size: 96px;
    line-height: 1;
    letter-spacing: 2px;
    color: var(--ink-navy);
  }
  .brand-rule {
    position: absolute;
    top: 262px;
    left: 140px;
    width: 560px;
    height: 4px;
    background: var(--ink-dark);
  }
  .product-name {
    position: absolute;
    top: 278px;
    left: 0;
    width: 100%;
    text-align: center;
    font-weight: 500;
    font-size: 40px;
    line-height: 1.2;
    color: var(--ink-dark);
  }
  .eco-claim {
    position: absolute;
    top: 338px;
    left: 0;
    width: 100%;
    text-align: center;
    font-weight: 500;
    font-size: 32px;
    line-height: 1.2;
    color: var(--eco-green);
  }
  .eco-emblem {
    position: absolute;
    top: 410px;
    left: 320px;
    width: 200px;
    height: 200px;
    border-radius: 50%;
    background: radial-gradient(circle, var(--eco-green-soft) 0%, var(--eco-green) 100%);
    opacity: 0.85;
  }
  .wave-field {
    position: absolute;
    left: 0;
    top: 640px;
    width: 100%;
    height: 470px;
    background: linear-gradient(180deg, var(--wave-light) 0%, var(--wave-mid) 45%, var(--wave-deep) 75%, var(--wave-mid) 100%);
    border-radius: 120px 40px 0 0 / 30px 20px 0 0;
  }
  .volume {
    position: absolute;
    right: 130px;
    top: 925px;
    font-weight: 500;
    font-size: 32px;
    line-height: 1.2;
    color: var(--white);
  }
</style>
</head>
<body>
  <main class="label">
    <h1 class="brand-name">SWIFT SERIES</h1>
    <div class="brand-rule"></div>
    <p class="product-name">SANITISING SPRAY &amp; WIPE</p>
    <p class="eco-claim">ENVIRONMENTALLY FRIENDLY</p>
    <div class="eco-emblem" role="img" aria-label="Green leaf and spiral eco emblem"></div>
    <div class="wave-field" role="img" aria-label="Layered blue ocean wave bands"></div>
    <p class="volume">500mL</p>
  </main>
</body>
</html>
```